I am looking for a business card design with the following info:

*I need the design to be in two sides one in English and the other in Arabic, and I want it horizontal design.
Please note that each side has to have the same information but one in English and the other in Arabic

Company Name: Wafir and وافر
Company Logo: Attached.
Company Activity: E rental cars And لخدمات تأجير السيارات الالكترونية
Company Snapchat: Dorqanet
Instagram Account: Dorqanet
Facebook Account: Dorqanet
Name: Tamer and تامر
Title: Manager and مدير
Location: Saudi Arabia - Riyadh and المملكة العربية السعودية - الرياض
Email : contact@wafir-rentals.example
Website: www.wafir-rentals.example
Mob #: +966-501234876
Tel #: +966-117654321

The design has to be in three colors only (Green, Black and White)

```html
<!DOCTYPE html>
<html lang="en">
<head>
<meta charset="utf-8">
<title>Wafir — Business Card</title>
<link rel="stylesheet" href="https://fonts.googleapis.com/css2?family=Open+Sans:wght@400;600;700&family=Cairo:wght@400;600;700&display=swap">
<style>
  :root {
    --green: #2fb351;
    --charcoal: #4a4a4a;
    --band: #3f3f3f;
    --ink: #333333;
    --muted: #6b6b6b;
    --paper: #f7f7f7;
    --backdrop: #3b3b3b;
    --footer-text: #c9c9c9;
  }
  * { box-sizing: border-box; margin: 0; padding: 0; }
  html, body { width: 1200px; height: 900px; overflow: hidden; }
  body {
    background: var(--backdrop);
    font-family: "Open Sans", Arial, sans-serif;
    display: flex;
    flex-direction: column;
    align-items: center;
    justify-content: center;
    gap: 40px;
  }
  .card {
    position: relative;
    width: 680px;
    height: 380px;
    border-radius: 24px;
    overflow: hidden;
    background: linear-gradient(180deg, #ffffff 0%, var(--paper) 100%);
    box-shadow: 0 10px 24px rgba(0,0,0,0.35);
  }
  .card__body {
    position: absolute;
    inset: 0 0 80px 0;
    display: flex;
    align-items: center;
  }
  .brand {
    width: 300px;
    display: flex;
    flex-direction: column;
    align-items: center;
    gap: 14px;
  }
  .brand__dot {
    width: 120px;
    height: 120px;
    border-radius: 50%;
    background: var(--green);
  }
  .brand__name {
    font-weight: 700;
    font-size: 24px;
    color: var(--green);
    letter-spacing: 1px;
  }
  .divider {
    width: 2px;
    height: 210px;
    background: var(--charcoal);
  }
  .details {
    padding-left: 22px;
    display: flex;
    flex-direction: column;
  }
  .person__name { font-size: 30px; font-weight: 700; color: var(--green); line-height: 1.1; }
  .person__title { font-size: 16px; color: var(--muted); margin-bottom: 6px; }
  .company__name { font-size: 20px; font-weight: 700; color: var(--green); line-height: 1.15; }
  .company__activity { font-size: 16px; color: var(--ink); margin-bottom: 12px; }
  .contacts { list-style: none; display: flex; flex-direction: column; gap: 5px; }
  .contact { display: flex; align-items: center; gap: 10px; font-size: 15px; color: var(--ink); }
  .contact svg { width: 16px; height: 16px; flex: none; fill: var(--green); }
  .social-square { width: 14px; height: 14px; background: var(--green); flex: none; margin: 0 1px; }
  .card__footer {
    position: absolute;
    left: 0; right: 0; bottom: 0;
    height: 80px;
    background: var(--band);
    border-top: 4px solid var(--green);
    display: flex;
    align-items: center;
    justify-content: center;
    color: var(--footer-text);
    font-size: 17px;
  }
  .card--arabic .rtl { font-family: "Cairo", Arial, sans-serif; direction: rtl; text-align: left; line-height: 1.3; }
  .card--arabic .person__title { margin-bottom: 2px; }
  .card--arabic .company__activity { font-size: 15px; margin-bottom: 8px; }
  .card--arabic .card__footer { font-family: "Cairo", Arial, sans-serif; direction: rtl; }
</style>
</head>
<body>

<section class="card card--arabic" lang="ar">
  <div class="card__body">
    <div class="brand">
      <div class="brand__dot"></div>
      <span class="brand__name" lang="en">Wafir</span>
    </div>
    <div class="divider"></div>
    <div class="details">
      <p class="person__name rtl">تامر</p>
      <p class="person__title rtl">مدير</p>
      <p class="company__name rtl">وافر</p>
      <p class="company__activity rtl">لخدمات تأجير السيارات الالكترونية</p>
      <ul class="contacts" lang="en">
        <li class="contact"><svg viewBox="0 0 24 24"><path d="M6.6 10.8a15.1 15.1 0 0 0 6.6 6.6l2.2-2.2a1 1 0 0 1 1-.25 11.4 11.4 0 0 0 3.6.57 1 1 0 0 1 1 1V20a1 1 0 0 1-1 1A17 17 0 0 1 3 4a1 1 0 0 1 1-1h3.5a1 1 0 0 1 1 1c0 1.25.2 2.45.57 3.57a1 1 0 0 1-.25 1z"/></svg><span>+966-117654321</span></li>
        <li class="contact"><svg viewBox="0 0 24 24"><path d="M7 1h10a2 2 0 0 1 2 2v18a2 2 0 0 1-2 2H7a2 2 0 0 1-2-2V3a2 2 0 0 1 2-2zm0 3v14h10V4zm5 15.5a1.2 1.2 0 1 0 0 2.4 1.2 1.2 0 0 0 0-2.4z"/></svg><span>+966-501234876</span></li>
        <li class="contact"><svg viewBox="0 0 24 24"><path d="M2 5h20v14H2zm2 2v.5l8 5 8-5V7zm0 2.8V17h16V9.8l-8 5z"/></svg><span>contact@wafir-rentals.example</span></li>
        <li class="contact"><svg viewBox="0 0 24 24"><path d="M12 2a10 10 0 1 0 0 20 10 10 0 0 0 0-20zm6.9 9h-3a15 15 0 0 0-1.3-6A8 8 0 0 1 18.9 11zM12 4.1c.9 1.3 1.7 3.6 1.9 6.9h-3.8c.2-3.3 1-5.6 1.9-6.9zM9.4 5a15 15 0 0 0-1.3 6h-3A8 8 0 0 1 9.4 5zM5.1 13h3a15 15 0 0 0 1.3 6A8 8 0 0 1 5.1 13zm6.9 6.9c-.9-1.3-1.7-3.6-1.9-6.9h3.8c-.2 3.3-1 5.6-1.9 6.9zm2.6-.9a15 15 0 0 0 1.3-6h3a8 8 0 0 1-4.3 6z"/></svg><span>www.wafir-rentals.example</span></li>
        <li class="contact"><span class="social-square"></span><span>Dorqanet</span></li>
      </ul>
    </div>
  </div>
  <footer class="card__footer">المملكة العربية السعودية - الرياض</footer>
</section>

<section class="card card--english">
  <div class="card__body">
    <div class="brand">
      <div class="brand__dot"></div>
      <span class="brand__name">Wafir</span>
    </div>
    <div class="divider"></div>
    <div class="details">
      <p class="person__name">Tamer</p>
      <p class="person__title">Manager</p>
      <p class="company__name">WAFIR</p>
      <p class="company__activity">E rental cars</p>
      <ul class="contacts">
        <li class="contact"><svg viewBox="0 0 24 24"><path d="M6.6 10.8a15.1 15.1 0 0 0 6.6 6.6l2.2-2.2a1 1 0 0 1 1-.25 11.4 11.4 0 0 0 3.6.57 1 1 0 0 1 1 1V20a1 1 0 0 1-1 1A17 17 0 0 1 3 4a1 1 0 0 1 1-1h3.5a1 1 0 0 1 1 1c0 1.25.2 2.45.57 3.57a1 1 0 0 1-.25 1z"/></svg><span>+966-117654321</span></li>
        <li class="contact"><svg viewBox="0 0 24 24"><path d="M7 1h10a2 2 0 0 1 2 2v18a2 2 0 0 1-2 2H7a2 2 0 0 1-2-2V3a2 2 0 0 1 2-2zm0 3v14h10V4zm5 15.5a1.2 1.2 0 1 0 0 2.4 1.2 1.2 0 0 0 0-2.4z"/></svg><span>+966-501234876</span></li>
        <li class="contact"><svg viewBox="0 0 24 24"><path d="M2 5h20v14H2zm2 2v.5l8 5 8-5V7zm0 2.8V17h16V9.8l-8 5z"/></svg><span>contact@wafir-rentals.example</span></li>
        <li class="contact"><svg viewBox="0 0 24 24"><path d="M12 2a10 10 0 1 0 0 20 10 10 0 0 0 0-20zm6.9 9h-3a15 15 0 0 0-1.3-6A8 8 0 0 1 18.9 11zM12 4.1c.9 1.3 1.7 3.6 1.9 6.9h-3.8c.2-3.3 1-5.6 1.9-6.9zM9.4 5a15 15 0 0 0-1.3 6h-3A8 8 0 0 1 9.4 5zM5.1 13h3a15 15 0 0 0 1.3 6A8 8 0 0 1 5.1 13zm6.9 6.9c-.9-1.3-1.7-3.6-1.9-6.9h3.8c-.2 3.3-1 5.6-1.9 6.9zm2.6-.9a15 15 0 0 0 1.3-6h3a8 8 0 0 1-4.3 6z"/></svg><span>www.wafir-rentals.example</span></li>
        <li class="contact"><span class="social-square"></span><span>Dorqanet</span></li>
      </ul>
    </div>
  </div>
  <footer class="card__footer">Saudi Arabia - Riyadh</footer>
</section>

</body>
</html>
```